Web Re-Design for African Art Gallery

Introduction
We are an art gallery carrying artworks by contemporary African artists. We require a new, more modern website for our gallery.
The website idea. The key words we’d like to use to describe our website are - elegant, simple, uncluttered, easy to navigate, classy, interesting.
We’d like a website that is as uncluttered as possible; a simple, elegant website that lets viewers carry out the business of viewing our artworks online as easily as possible. A web site that is adventurous and arty without being complicated.
Our logo is a monochrome dark grey colour but this should not affect the colour scheme of the website. We are also open to a new logo if it is decidedly better than what we have at present, and would be willing to pay additionally for it if we take it.
Our audience is international. Art collectors worldwide looking for contemporary art. We do not want any African themed design.
Sections
The home page will have various sections – Artists, New Works, Publication, Mailing list, Exhibitions
Below are a list of gallery websites we like.
http://www.dorvantelis.example/
http://www.pembrickgallery.example/
http://www.wyattolandor.example/
http://www.quillbaneart.example/exhibitions/2011-12-13_tidal-murmurs/
http://www.zpo.vrnt.example/index.html
Requirement
We'd like a a home page template as well as a template for the sections in HTML.
We do not have a regular coder so we'd be happy to have the winning designer carry on with fitting the rest of the site to the template if the price is right.
Our present website is www.lanternreefgallery.example. feel free to get logo, artwork pictures and any other material you might need from there.
Thanks

```html
<!DOCTYPE html>
<html lang="en">
<head>
<meta charset="utf-8">
<title>Lantern Reef Gallery – The Artists</title>
<link href="https://fonts.googleapis.com/css2?family=Open+Sans:wght@400;600;700&family=Tinos&family=Arimo&display=swap" rel="stylesheet">
<style>
:root{
  --page:#efefef;
  --black:#050505;
  --white:#ffffff;
  --text:#333333;
  --muted:#666666;
  --green:#7cc21f;
  --green-dark:#4f8f0e;
  --green-light:#a6de44;
  --artist:#5b6b20;
  --red:#c00000;
  --link:#1a1aa6;
  --line:#cfcfcf;
  --bubble:#9a9a9a;
  --cyan:#4fc3e8;
  --footer:#dcdcdc;
}
*{box-sizing:border-box;margin:0;padding:0}
html,body{width:1016px;height:1200px;overflow:hidden}
body{position:relative;background:var(--page);font-family:"Open Sans",sans-serif;color:var(--text)}
.abs{position:absolute}
.topbar{left:0;top:0;width:1016px;height:15px;background:var(--black)}
.contact{top:36px;left:706px;font-size:12px;font-weight:700;display:flex;align-items:center;gap:6px;color:#222}
.live-help{top:36px;left:835px;font-size:12px;font-weight:700;color:#e0301e;display:flex;align-items:center;gap:6px}
.logo{left:56px;top:56px;width:141px;height:53px;background:var(--white);border:2px solid #222;box-shadow:2px 2px 3px #999;display:flex;align-items:center;justify-content:center;text-align:center;font-size:13px;font-weight:700;color:#333;line-height:1.1}
.nav{left:254px;top:73px;width:681px;height:38px;background:linear-gradient(#fbfbfb,#e6e6e6);border:1px solid #ccc;border-radius:10px;box-shadow:0 2px 3px #bbb;display:flex;align-items:center;padding-left:14px;font-size:13px;color:#666}
.nav a{color:#666;text-decoration:none;padding:0 12px;border-right:1px solid #d6d6d6;line-height:22px;display:flex;align-items:center;gap:6px}
.search{position:absolute;right:14px;top:7px;width:180px;height:24px;border:1px solid #ccc;border-radius:12px;background:var(--white);font-size:10px;font-style:italic;color:#aaa;padding:5px 12px}
.search-btn{position:absolute;right:-1px;top:-1px;width:28px;height:24px;border-radius:0 12px 12px 0;background:var(--green);display:flex;align-items:center;justify-content:center}
.sidebar{left:20px;top:134px;width:202px;height:930px;background:var(--page);border:1px solid #d0d0d0;box-shadow:1px 1px 2px #bbb}
.ribbon{left:0;top:128px}
.ribbon-title{left:0;top:141px;width:240px;text-align:center;font-size:16px;font-weight:700;color:var(--white)}
.artists{left:68px;top:190px;list-style:none}
.artists li{height:26.9px;font-size:13px;color:var(--artist);display:flex;align-items:center;gap:14px}
.main{left:236px;top:139px;width:741px;height:925px;background:var(--white);border-radius:8px}
.sortbar{left:279px;top:161px;font-size:11px;color:#555;display:flex;align-items:center;gap:6px}
.select{height:17px;border:1px solid #bbb;display:flex;align-items:center;padding-left:4px;font-size:11px;color:#555;position:relative}
.select i{position:absolute;right:0;top:0;width:16px;height:15px;background:#333}
.select i::after{content:"";position:absolute;left:4px;top:6px;border:4px solid transparent;border-top-color:#fff}
.perpage{left:736px;top:162px;font-size:11px;color:#555}
.perpage b{font-weight:400;color:var(--red)}
.perpage span{color:#888}
.art{width:122px;border-radius:4px;box-shadow:2px 3px 3px #999}
.art.portrait{height:88px;background:linear-gradient(110deg,#3d5a2a 0%,#6b5a4a 35%,#d07a9e 60%,#e5a7c9 80%,#7d6ea8 100%)}
.art.masks{height:76px;background:linear-gradient(90deg,#35467a 0%,#2b7a3e 30%,#4762a3 55%,#a13a5a 80%,#5a6db0 100%)}
.art.land{height:80px;background:linear-gradient(#8a3a20 0%,#c0602c 40%,#d88046 55%,#6a2a1a 75%,#b05a34 100%)}
.caption{font-family:"Tinos",serif;font-size:11px;color:var(--link);text-decoration:underline}
.pager{left:550px;top:686px;font-size:11px;color:var(--red);display:flex;gap:10px;align-items:center}
.pager .current{background:var(--red);color:#fff;width:19px;height:18px;display:flex;align-items:center;justify-content:center}
.rule{left:315px;top:709px;width:632px;border-top:1px solid var(--line)}
.heading{font-size:13px;color:#333;display:flex;align-items:center;gap:6px}
.heading i{width:16px;height:16px;background:var(--cyan);border-radius:3px;display:flex;align-items:center;justify-content:center}
.follow{left:535px;top:734px;font-size:9px;color:var(--cyan)}
.heading-rule{border-top:1px solid var(--line)}
.tweet{left:274px;width:302px;background:var(--bubble);border-radius:4px;font-family:"Arimo",sans-serif;font-size:9.5px;color:#fff;padding:8px 10px;line-height:13px}
.tweet::before{content:"";position:absolute;left:12px;top:-10px;border-left:0 solid transparent;border-right:14px solid transparent;border-bottom:10px solid var(--bubble)}
.tweet span{color:#9ee3ff}
.recent{width:52px;height:52px}
.net{width:52px;height:52px;border-radius:6px;box-shadow:1px 2px 3px #999}
.footer{left:0;top:1109px;width:1016px;height:91px;background:var(--footer)}
.footer-links{left:31px;top:1137px;font-size:11px;color:#444}
.copyright{left:31px;top:1155px;font-size:11px;color:#444}
.footer-logo{left:766px;top:1127px;width:146px;height:56px}
</style>
</head>
<body>
<div class="abs topbar"></div>

<div class="abs contact">
  <svg width="16" height="18" viewBox="0 0 16 18"><path d="M3 1 L6 1 L7 5 L5 7 Q7 11 10 13 L12 11 L15 13 L15 16 Q12 18 8 15 Q2 10 2 4 Z" fill="#e0701e"/></svg>
  234-8000555012
</div>
<div class="abs live-help">
  <svg width="30" height="18" viewBox="0 0 30 18"><ellipse cx="15" cy="8" rx="14" ry="7" fill="#7cc21f"/><path d="M12 14 L10 18 L17 14 Z" fill="#7cc21f"/></svg>
  Live Help
</div>

<div class="abs logo">Lantern Reef<br>Gallery</div>

<nav class="abs nav">
  <a href="#"><svg width="14" height="13" viewBox="0 0 14 13"><path d="M7 0 L14 6 L12 6 L12 13 L8.5 13 L8.5 9 L5.5 9 L5.5 13 L2 13 L2 6 L0 6 Z" fill="#777"/></svg>Home</a>
  <a href="#">About</a>
  <a href="#">Services</a>
  <a href="#">Articles</a>
  <a href="#">Gallery</a>
  <a href="#">Exhibitions</a>
  <div class="search">search...
    <div class="search-btn"><svg width="12" height="12" viewBox="0 0 12 12"><circle cx="5" cy="5" r="3.5" fill="none" stroke="#fff" stroke-width="1.6"/><path d="M7.5 7.5 L11 11" stroke="#fff" stroke-width="2"/></svg></div>
  </div>
</nav>

<aside class="abs sidebar"></aside>
<svg class="abs ribbon" width="240" height="44" viewBox="0 0 240 44">
  <path d="M0 2 L24 2 L24 34 L0 34 L10 18 Z" fill="var(--green-dark)"/>
  <path d="M240 2 L216 2 L216 34 L240 34 L230 18 Z" fill="var(--green-dark)"/>
  <rect x="18" y="6" width="204" height="34" fill="var(--green)"/>
  <rect x="18" y="6" width="204" height="14" fill="var(--green-light)" opacity="0.6"/>
</svg>
<div class="abs ribbon-title">The Artists</div>

<ul class="abs artists">
  <li>Tamuno Ekwerebi <svg width="16" height="10" viewBox="0 0 16 10"><path d="M1 1 L6 5 L1 9 M8 1 L13 5 L8 9" fill="none" stroke="#8a8ab0" stroke-width="2"/></svg></li>
  <li>Kojo Brevanti</li>
  <li>Lanre Osidemi</li>
  <li>Femi Daranko</li>
  <li>Ayodeji Marrow</li>
  <li>Tunde Ebarin</li>
  <li>Chike Onwelu</li>
  <li>Kweku Amaltey</li>
  <li>Sadiq Ilemoro</li>
  <li>Bayo Kestrel</li>
  <li>Dele Fairholm</li>
  <li>Efe Oruvwerha</li>
  <li>Zeno Ariwa</li>
  <li>Osaro Benwell</li>
  <li>Kunle Ashiwaju</li>
  <li>Eseosa Vroati</li>
  <li>Rasaki Oyelaro</li>
  <li>Irene Wadoje</li>
  <li>Nosa Ighodaro</li>
  <li>Gideon Hale</li>
  <li>Daniel Dorne</li>
  <li>Obinna Nwankpa</li>
  <li>Mordi Zebulon</li>
  <li>Yemi Mobolaji</li>
  <li>Ben Aiyekoro</li>
  <li>Chioma Ilodi</li>
  <li>Daniel Dorne</li>
  <li>Rasheed Amadu</li>
  <li>Taiwo Olajire</li>
  <li>Biodun Olawande</li>
  <li>Jide Buremo</li>
  <li>Jonah Afolarin</li>
</ul>

<main class="abs main"></main>

<div class="abs sortbar">Sort by:
  <div class="select" style="width:104px">Ascending<i></i></div>
  <div class="select" style="width:108px;margin-left:8px">Product Name<i></i></div>
  <div class="select" style="width:108px;margin-left:8px">Brand Name<i></i></div>
</div>
<div class="abs perpage">Items per page: &nbsp; <span>12 &nbsp;/&nbsp; 20 &nbsp;/</span> <b>30</b> <b>&nbsp;/ 50</b></div>

<!-- row 1 -->
<div class="abs art portrait" style="left:280px;top:228px" role="img" aria-label="Painting of a figure in pink and green tones"></div>
<div class="abs art portrait" style="left:457px;top:232px" role="img" aria-label="Painting of a figure in pink and green tones"></div>
<div class="abs art portrait" style="left:648px;top:232px" role="img" aria-label="Painting of a figure in pink and green tones"></div>
<div class="abs art portrait" style="left:819px;top:232px" role="img" aria-label="Painting of a figure in pink and green tones"></div>
<div class="abs caption" style="left:280px;top:329px">Ayodeji Marrow</div>
<div class="abs caption" style="left:457px;top:333px">Ayodeji Marrow</div>
<div class="abs caption" style="left:648px;top:334px">Ayodeji Marrow</div>
<div class="abs caption" style="left:819px;top:333px">Ayodeji Marrow</div>

<!-- row 2 -->
<div class="abs art masks" style="left:282px;top:389px" role="img" aria-label="Colourful painting of standing figures in blue and green"></div>
<div class="abs art masks" style="left:459px;top:393px" role="img" aria-label="Colourful painting of standing figures in blue and green"></div>
<div class="abs art masks" style="left:650px;top:393px" role="img" aria-label="Colourful painting of standing figures in blue and green"></div>
<div class="abs art masks" style="left:821px;top:393px" role="img" aria-label="Colourful painting of standing figures in blue and green"></div>
<div class="abs caption" style="left:280px;top:481px">Ben Aiyekoro</div>
<div class="abs caption" style="left:457px;top:485px">Ben Aiyekoro</div>
<div class="abs caption" style="left:648px;top:486px">Ben Aiyekoro</div>
<div class="abs caption" style="left:819px;top:485px">Ben Aiyekoro</div>

<!-- row 3 -->
<div class="abs art land" style="left:282px;top:539px" role="img" aria-label="Warm landscape painting with a village at dusk"></div>
<div class="abs art land" style="left:459px;top:543px" role="img" aria-label="Warm landscape painting with a village at dusk"></div>
<div class="abs art land" style="left:650px;top:543px" role="img" aria-label="Warm landscape painting with a village at dusk"></div>
<div class="abs art land" style="left:821px;top:543px" role="img" aria-label="Warm landscape painting with a village at dusk"></div>
<div class="abs caption" style="left:280px;top:633px">Zeno Ariwa</div>
<div class="abs caption" style="left:457px;top:637px">Zeno Ariwa</div>
<div class="abs caption" style="left:648px;top:638px">Zeno Ariwa</div>
<div class="abs caption" style="left:819px;top:637px">Zeno Ariwa</div>

<div class="abs pager"><span class="current">1</span><span>2</span><span>3</span><span>4</span><span>5</span><span>Next &gt;</span><span>&nbsp;Last &gt;&gt;</span></div>
<div class="abs rule"></div>

<!-- latest tweets -->
<div class="abs heading" style="left:275px;top:726px"><i><svg width="10" height="10" viewBox="0 0 12 12"><circle cx="5" cy="5" r="3.5" fill="none" stroke="#fff" stroke-width="1.6"/><path d="M7.5 7.5 L11 11" stroke="#fff" stroke-width="2"/></svg></i>LATEST TWEETS</div>
<div class="abs follow">follow me</div>
<div class="abs heading-rule" style="left:275px;top:747px;width:302px"></div>
<div class="abs tweet" style="top:767px;height:44px">Follow Top Graphic Designers on Twitter to Boost Your Career<br><span>http://FFFFFFFFFF</span></div>
<div class="abs tweet" style="top:831px;height:31px;padding-top:9px">RT @<span>FFFFFFFFFFFFFFFFFFFFFFFFFFFFFF</span></div>
<div class="abs tweet" style="top:883px;height:44px">CCCCCCCCCCCCCCCCCCCCCCCCCCCCCCCCCCCCCCCCCC CCCCCCCCCCCC</div>

<!-- recent -->
<div class="abs heading" style="left:637px;top:730px"><i><svg width="10" height="10" viewBox="0 0 12 12"><circle cx="5" cy="5" r="3.5" fill="none" stroke="#fff" stroke-width="1.6"/><path d="M7.5 7.5 L11 11" stroke="#fff" stroke-width="2"/></svg></i>RECENT</div>
<div class="abs heading-rule" style="left:637px;top:751px;width:302px"></div>
<div class="abs recent" style="left:635px;top:762px;background:linear-gradient(#f4f4f4,#7fd1d1)" role="img" aria-label="Recent post preview"></div>
<div class="abs recent" style="left:697px;top:762px;background:linear-gradient(135deg,#e8f4fb,#2a9ad6)" role="img" aria-label="Recent post preview"></div>
<div class="abs recent" style="left:759px;top:762px;background:linear-gradient(#f2f2f2,#9a9a9a)" role="img" aria-label="Recent post preview"></div>
<div class="abs recent" style="left:822px;top:762px;background:linear-gradient(#7cc21f 0%,#7cc21f 30%,#333 31%,#888)" role="img" aria-label="Recent post preview"></div>
<div class="abs recent" style="left:885px;top:762px;background:linear-gradient(#333 0%,#333 20%,#f6f6f6 21%);border-left:2px solid #f08a00;border-right:2px solid #f08a00" role="img" aria-label="Recent post preview"></div>

<!-- network -->
<div class="abs heading" style="left:637px;top:838px"><i><svg width="10" height="10" viewBox="0 0 12 12"><circle cx="5" cy="5" r="3.5" fill="none" stroke="#fff" stroke-width="1.6"/><path d="M7.5 7.5 L11 11" stroke="#fff" stroke-width="2"/></svg></i>NETWORK</div>
<div class="abs heading-rule" style="left:637px;top:859px;width:302px"></div>
<div class="abs net" style="left:635px;top:869px;background:linear-gradient(#5fd0ee,#1a9fc9)" role="img" aria-label="Network link"></div>
<div class="abs net" style="left:697px;top:869px;background:linear-gradient(#ffffff,#d0d0d0)" role="img" aria-label="Network link"></div>
<div class="abs net" style="left:760px;top:869px;background:linear-gradient(#2e6fc4,#0d3f8a)" role="img" aria-label="Network link"></div>
<div class="abs net" style="left:824px;top:869px;background:linear-gradient(#8ee04a,#3f9a10)" role="img" aria-label="Network link"></div>
<div class="abs net" style="left:888px;top:869px;background:linear-gradient(#6d8fd0,#3b5a9a)" role="img" aria-label="Network link"></div>

<footer class="abs footer"></footer>
<div class="abs footer-links">Home &nbsp;|&nbsp; About Us &nbsp;|&nbsp; Portfolio &nbsp;|&nbsp; Services &nbsp;|&nbsp; Blog &nbsp;|&nbsp; Contact Us</div>
<div class="abs copyright">© 2012 XXXXXX. All Rights Reserved</div>
<div class="abs logo footer-logo">Lantern Reef<br>Gallery</div>
</body>
</html>
```